Info Graphic for Luminous Stride Academy

WELCOME To The Luminous Stride Academy (LSA)

We are wanting to create a visual info graphic display of a newly designed transformational pathway program.

Please display the following heading:

The Luminous Stride Academy (LSA) Pathway Program

Subheading:

“Feeling alive and living the life you want to be living.”

Please display each step along the path clearly and with visuals representations that reflect the energy of the word and achievement accomplished.

We would like to display each step individually whilst tying to capture a flow of progression whilst maintaining the look and feel of each step.

The infographic design wants to really spark people’s attention, create impact and a curiosity resulting in a desire to seek more information regarding the program.

Energetic vibrant colours and flow are a must.

A sense of Playfulness, fun and energy is what we are looking for with this design.

The pathway is progressive with each step building on the last and I would like this to be represented in a linear fashion and NOT show steps as hierarchical.

The below documents the steps in order of progression and describes the key focus and outcome for each of the steps.

THE LSA PATHWAY:

Step 1: Intriguing You - Discover the path to transformation and igniting your relationships and life.

Step 2: Energizing You - Introduction to the Foundational principles.

Step 3: Awakening You - Creating juicy, deep connections with self and others.

Step 4: Transforming You - Feeling alive and creating a life of clarity and flow.

Step 5: Igniting You - Discovering that “This S**T Works” by living the life you want to be living.

Additional Modules available at Transforming You (by invitation)

Additional Step: Launching You - Learn to share the principles and tools to facilitate the LSA Path for family, friends and clients.

Additional Step: Aligning You - How do couples co-create a relationship that is on fire with passion and expression?

I have attached a previous style guide that we have utilised however don’t want to be limited to just this in the designs.

Happy for this to be utilised and included in designs and we are very open to do something completely different, please be creative.

Any questions or further information required, please let me know.

Target Market(s)

People looking to Feel alive and living the life you want to be living

Industry/Entity Type

Relationship and Personal Development

Requirements
Must have
• Creativity
Nice to have
• Linear display of steps and the explanations at each step included in the description
Should not have
• display hierarchy

```html
<!DOCTYPE html>
<html lang="en">
<head>
<meta charset="utf-8">
<title>Luminous Stride Academy – Pathway Program</title>
<link href="https://fonts.googleapis.com/css2?family=Open+Sans:ital,wght@0,400;0,600;0,700;1,400&display=swap" rel="stylesheet">
<style>
  :root {
    --step-1: #f8ee1c;
    --step-2: #fbc82c;
    --step-3: #c8a3cf;
    --step-4: #7b12c8;
    --step-5: #0a37b6;
    --step-6: #0b9ad6;
    --step-8: #5ac8e9;
    --label-ink: #7a2bc0;
    --body-ink: #5a5a5a;
    --title-ink: #3c3c3c;
    --brand-ink: #111111;
    --brand-dot: #8a4fd8;
    --paper: #ffffff;
  }
  html, body {
    margin: 0;
    padding: 0;
    overflow: hidden;
    background: var(--paper);
  }
  .canvas {
    position: relative;
    width: 1200px;
    height: 1200px;
    overflow: hidden;
    background: var(--paper);
    font-family: "Open Sans", Arial, sans-serif;
  }
  .program-header {
    position: absolute;
    left: 0;
    top: 58px;
    width: 1200px;
    text-align: center;
  }
  .program-title {
    margin: 0;
    font-size: 34px;
    line-height: 42px;
    font-weight: 700;
    color: var(--title-ink);
  }
  .program-subtitle {
    margin: 10px 0 0;
    font-size: 20px;
    line-height: 26px;
    font-style: italic;
    font-weight: 400;
    color: var(--label-ink);
  }
  .pathway {
    position: absolute;
    inset: 0;
    width: 1200px;
    height: 1200px;
  }
  .step-tag {
    font-family: "Open Sans", Arial, sans-serif;
    font-weight: 700;
    font-size: 8px;
    fill: var(--label-ink);
  }
  .step-copy {
    position: absolute;
    margin: 0;
    width: 240px;
    font-size: 13px;
    line-height: 17px;
    color: var(--body-ink);
  }
  .step-copy .step-name {
    font-weight: 700;
    color: var(--title-ink);
  }
  .brand {
    position: absolute;
    left: 112px;
    top: 862px;
    display: flex;
    align-items: center;
    gap: 18px;
  }
  .brand-dot {
    width: 58px;
    height: 58px;
    border-radius: 50%;
    background: var(--brand-dot);
  }
  .brand-name {
    margin: 0;
    font-family: "Open Sans", Arial, sans-serif;
    font-weight: 600;
    font-size: 40px;
    line-height: 46px;
    letter-spacing: 2px;
    color: var(--brand-ink);
  }
</style>
</head>
<body>
<main class="canvas">
  <header class="program-header">
    <h1 class="program-title">The Luminous Stride Academy (LSA) Pathway Program</h1>
    <p class="program-subtitle">“Feeling alive and living the life you want to be living.”</p>
  </header>

  <svg class="pathway" viewBox="0 0 1000 1000" xmlns="http://www.w3.org/2000/svg">
    <g class="step step-8" transform="translate(-542 -515)">
      <polygon fill="var(--step-8)" points="560,868 778,868 808,837 612,837 690,730 705,748 720,690 665,700 682,716 560,845"/>
    </g>
    <g class="step step-6" transform="translate(-453 -430)">
      <polygon fill="var(--step-6)" points="580,857 778,857 808,837 612,837 655,795 665,808 672,768 630,772 642,782 580,845"/>
    </g>
    <g class="step step-5" transform="translate(-365 -345)">
      <polygon fill="var(--step-5)" points="580,857 778,857 808,837 612,837 655,795 665,808 672,768 630,772 642,782 580,845"/>
    </g>
    <g class="step step-4" transform="translate(-278 -260)">
      <polygon fill="var(--step-4)" points="580,857 778,857 808,837 612,837 655,795 665,808 672,768 630,772 642,782 580,845"/>
    </g>
    <g class="step step-3" transform="translate(-193 -170)">
      <polygon fill="var(--step-3)" points="580,857 778,857 808,837 612,837 655,795 665,808 672,768 630,772 642,782 580,845"/>
    </g>
    <g class="step step-2" transform="translate(-108 -85)">
      <polygon fill="var(--step-2)" points="580,857 778,857 808,837 612,837 655,795 665,808 672,768 630,772 642,782 580,845"/>
    </g>
    <g class="step step-1">
      <polygon fill="var(--step-1)" points="580,857 910,857 940,837 612,837 655,795 665,808 672,768 630,772 642,782 580,845"/>
    </g>

    <g class="marker" transform="translate(-542 -515)">
      <line x1="768" y1="792" x2="768" y2="837" stroke="var(--step-8)" stroke-width="4"/>
      <rect x="768" y="804" width="38" height="16" fill="#fff" stroke="var(--step-8)" stroke-width="1.5"/>
      <text class="step-tag" x="774" y="815">STEP 8</text>
      <circle cx="768" cy="770" r="22" fill="#fff" stroke="var(--step-8)" stroke-width="5"/>
      <circle cx="768" cy="770" r="14" fill="#e6f6fb" role="img" aria-label="Head icon with a heart, couples in alignment"/>
    </g>
    <g class="marker" transform="translate(-453 -430)">
      <line x1="768" y1="792" x2="768" y2="837" stroke="var(--step-6)" stroke-width="4"/>
      <rect x="768" y="804" width="38" height="16" fill="#fff" stroke="var(--step-6)" stroke-width="1.5"/>
      <text class="step-tag" x="774" y="815">STEP 6</text>
      <circle cx="768" cy="770" r="22" fill="#fff" stroke="var(--step-6)" stroke-width="5"/>
      <circle cx="768" cy="770" r="14" fill="#e3f3fa" role="img" aria-label="Head icon with a rocket, launching"/>
    </g>
    <g class="marker" transform="translate(-365 -345)">
      <line x1="768" y1="792" x2="768" y2="837" stroke="var(--step-5)" stroke-width="4"/>
      <rect x="768" y="804" width="38" height="16" fill="#fff" stroke="var(--step-5)" stroke-width="1.5"/>
      <text class="step-tag" x="774" y="815">STEP 5</text>
      <circle cx="768" cy="770" r="22" fill="#fff" stroke="var(--step-5)" stroke-width="5"/>
      <circle cx="768" cy="770" r="14" fill="#e4e9f7" role="img" aria-label="Head icon with rising flames, igniting"/>
    </g>
    <g class="marker" transform="translate(-278 -260)">
      <line x1="768" y1="792" x2="768" y2="837" stroke="var(--step-4)" stroke-width="4"/>
      <rect x="768" y="804" width="38" height="16" fill="#fff" stroke="var(--step-4)" stroke-width="1.5"/>
      <text class="step-tag" x="774" y="815">STEP 4</text>
      <circle cx="768" cy="770" r="22" fill="#fff" stroke="var(--step-4)" stroke-width="5"/>
      <circle cx="768" cy="770" r="14" fill="#efe3f8" role="img" aria-label="Head icon inside a turning arrow, transforming"/>
    </g>
    <g class="marker" transform="translate(-193 -170)">
      <line x1="768" y1="792" x2="768" y2="837" stroke="var(--step-3)" stroke-width="4"/>
      <rect x="768" y="804" width="38" height="16" fill="#fff" stroke="var(--step-3)" stroke-width="1.5"/>
      <text class="step-tag" x="774" y="815">STEP 3</text>
      <circle cx="768" cy="770" r="22" fill="#fff" stroke="var(--step-3)" stroke-width="5"/>
      <circle cx="768" cy="770" r="14" fill="#f5edf6" role="img" aria-label="Head icon with light rays, awakening"/>
    </g>
    <g class="marker" transform="translate(-108 -85)">
      <line x1="768" y1="792" x2="768" y2="837" stroke="var(--step-2)" stroke-width="4"/>
      <rect x="768" y="804" width="38" height="16" fill="#fff" stroke="var(--step-2)" stroke-width="1.5"/>
      <text class="step-tag" x="774" y="815">STEP 2</text>
      <circle cx="768" cy="770" r="22" fill="#fff" stroke="var(--step-2)" stroke-width="5"/>
      <circle cx="768" cy="770" r="14" fill="#fdf3d6" role="img" aria-label="Head icon with a lightning bolt, energizing"/>
    </g>
    <g class="marker">
      <line x1="768" y1="792" x2="768" y2="837" stroke="var(--step-1)" stroke-width="4"/>
      <rect x="768" y="804" width="38" height="16" fill="#fff" stroke="var(--step-1)" stroke-width="1.5"/>
      <text class="step-tag" x="774" y="815">STEP 1</text>
      <circle cx="768" cy="770" r="22" fill="#fff" stroke="var(--step-1)" stroke-width="5"/>
      <circle cx="768" cy="770" r="14" fill="#fdfbd8" role="img" aria-label="Head icon with a question mark, intriguing"/>
    </g>
  </svg>

  <p class="step-copy" style="left:316px; top:276px;"><span class="step-name">Aligning You -</span> How do couples co-create a relationship that is on fire with passion and expression?.</p>
  <p class="step-copy" style="left:420px; top:379px; width:250px;"><span class="step-name">Launching You -</span> Learn to share the principles and tools to facilitate the LSA Path for family, friends and clients.</p>
  <p class="step-copy" style="left:524px; top:483px;"><span class="step-name">Igniting You -</span> Discovering that “This S**T Works” by living the life you want to be living.</p>
  <p class="step-copy" style="left:631px; top:596px;"><span class="step-name">Transforming You -</span> Feeling alive and creating a life of clarity and flow.</p>
  <p class="step-copy" style="left:736px; top:702px;"><span class="step-name">Awakening You -</span> Creating juicy, deep connections with self and others.</p>
  <p class="step-copy" style="left:845px; top:802px;"><span class="step-name">Energizing You -</span> Introduction to the Foundational principles.</p>
  <p class="step-copy" style="left:949px; top:898px; width:232px;"><span class="step-name">Intriguing You -</span> Discover the path to transformation and igniting your relationships and life.</p>

  <div class="brand">
    <span class="brand-dot"></span>
    <p class="brand-name">Luminous<br>Stride<br>Academy</p>
  </div>
</main>
</body>
</html>
```